Tolvex Engineers: Why you should hire us keepsake

New design. Open to plastic cards. We are an engineering firm that designs cell phone towers and commercial buildings. Please check out our website www.tolvexgrp.com for more details. We want people to remember our card and for it to be useful if possible. We want the same look and feel on these cards to be translated to other marketing material we may need such as brochures.

Target Market(s)

Architects, Developers and Telecommunication Carriers

Industry/Entity Type

Engineering

Contact Information for Business Card

Card with our company colors, logo, and innovative design with elements related to our industry.

Font styles to use
Sans Serif

Colors
9bcb3c
abd036
0255a3

Requirements
Must have
• Sleek and hip design
Nice to have
• Bright lime green and navy coloring that pops with an innovative design.
Should not have
• A basic and boring design

```html
<!DOCTYPE html>
<html lang="en">
<head>
<meta charset="utf-8">
<title>Tolvex Engineers – Business Card</title>
<link href="https://fonts.googleapis.com/css2?family=Montserrat:wght@400;500;800&display=swap" rel="stylesheet">
<style>
  :root {
    --lime: #33e61a;
    --navy: #0a3466;
    --navy-deep: #072a57;
    --navy-light: #123f78;
    --white: #ffffff;
    --stage: #e9e9ea;
  }
  * { box-sizing: border-box; margin: 0; padding: 0; }
  html, body { width: 1200px; height: 1000px; overflow: hidden; }
  body {
    background: var(--stage);
    font-family: "Montserrat", Arial, sans-serif;
    position: relative;
  }
  .card {
    position: absolute;
    left: 270px;
    width: 660px;
    border-radius: 18px;
    overflow: hidden;
    box-shadow: 0 6px 14px rgba(0,0,0,0.28);
  }
  .card-front {
    top: 110px;
    height: 375px;
    background: linear-gradient(180deg, #ffffff 0%, #f6fbf5 100%);
  }
  .front-wordmark {
    position: absolute;
    left: 0; right: 0; top: 215px;
    transform: translateY(-50%);
    text-align: center;
    font-weight: 800;
    font-size: 118px;
    letter-spacing: -3px;
    color: var(--lime);
    line-height: 1;
  }
  .front-web {
    position: absolute;
    left: 0; right: 0; top: 327px;
    text-align: center;
    font-size: 14px;
    color: var(--navy);
  }
  .front-web .accent, .back-web .accent { color: var(--lime); }

  .card-back {
    top: 522px;
    height: 378px;
    background: linear-gradient(160deg, var(--navy-light) 0%, var(--navy) 45%, var(--navy-deep) 100%);
    color: var(--white);
  }
  .back-wordmark {
    position: absolute;
    left: 44px; top: 46px;
    font-weight: 800;
    font-size: 92px;
    letter-spacing: -2px;
    color: var(--lime);
    line-height: 1;
  }
  .holder-name {
    position: absolute;
    left: 36px; top: 197px;
    font-size: 20px;
    color: var(--lime);
  }
  .divider {
    position: absolute;
    left: 36px; right: 38px; top: 231px;
    height: 1px;
    background: rgba(255,255,255,0.18);
  }
  .contact-list {
    position: absolute;
    left: 38px; top: 243px;
    list-style: none;
    font-size: 15px;
    line-height: 21.5px;
  }
  .contact-list li { display: flex; align-items: center; gap: 6px; }
  .contact-list svg { width: 11px; height: 11px; fill: var(--lime); }
  .address {
    position: absolute;
    right: 37px; top: 244px;
    text-align: right;
    font-size: 15px;
    line-height: 20px;
  }
  .back-web {
    position: absolute;
    right: 37px; top: 289px;
    font-size: 15px;
  }
  .tagline-band {
    position: absolute;
    left: 0; right: 0; top: 324px;
    height: 31px;
    background: var(--white);
  }
  .tagline-band .flag {
    position: absolute;
    left: 0; top: 0;
    width: 38px; height: 31px;
  }
  .tagline-band .tagline {
    position: absolute;
    left: 53px; top: 6px;
    font-size: 15px;
    color: var(--navy);
  }
</style>
</head>
<body>
  <section class="card card-front" aria-label="Card front">
    <div class="front-wordmark">Tolvex</div>
    <div class="front-web">www.<span class="accent">tolvexgrp</span>.com</div>
  </section>

  <section class="card card-back" aria-label="Card back">
    <div class="back-wordmark">Tolvex</div>
    <div class="holder-name">Dana Riley Hollis</div>
    <div class="divider"></div>
    <ul class="contact-list">
      <li>
        <svg viewBox="0 0 24 24" aria-hidden="true"><path d="M6.6 10.8a15.1 15.1 0 0 0 6.6 6.6l2.2-2.2c.3-.3.7-.4 1-.2 1.1.4 2.3.6 3.6.6.6 0 1 .4 1 1V20c0 .6-.4 1-1 1A17 17 0 0 1 3 4c0-.6.4-1 1-1h3.5c.6 0 1 .4 1 1 0 1.3.2 2.5.6 3.6.1.3 0 .7-.2 1z"/></svg>
        555.014.2290
      </li>
      <li>
        <svg viewBox="0 0 24 24" aria-hidden="true"><path d="M7 1h10a2 2 0 0 1 2 2v18a2 2 0 0 1-2 2H7a2 2 0 0 1-2-2V3a2 2 0 0 1 2-2zm0 3v14h10V4zm5 15.5a1.2 1.2 0 1 0 0 2.4 1.2 1.2 0 0 0 0-2.4z"/></svg>
        555.014.7731
      </li>
      <li>
        <svg viewBox="0 0 24 24" aria-hidden="true"><path d="M2 5h20v14H2zm2 2v.5l8 5 8-5V7zm0 2.8V17h16V9.8l-8 5z"/></svg>
        dhollis@tolvexgrp.com
      </li>
    </ul>
    <div class="address">2400 Larkfield Commons Dr.<br>Suite 310 Halvern, GA 30999</div>
    <div class="back-web">www.<span class="accent">tolvexgrp</span>.com</div>
    <div class="tagline-band">
      <svg class="flag" viewBox="0 0 38 31" aria-hidden="true"><polygon points="0,0 38,0 28,31 0,31" fill="var(--lime)"/></svg>
      <span class="tagline">Multi-discipline engineering</span>
    </div>
  </section>
</body>
</html>
```